Brindlecove - Healthcare Brochure - B2B

We need a new brochure design, we're satisfied with the copy but were just looking for complete overhaul of the design. Please see an example of the old design attached. It was just a template we filled out.
Requirements
Nice to have
- The second attachment is an example of a style we like

```html
<!DOCTYPE html>
<html lang="en">
<head>
<meta charset="UTF-8">
<title>Brindlecove Post-Acute Care Brochure</title>
<link href="https://fonts.googleapis.com/css2?family=Poppins:ital,wght@0,400;0,500;0,600;0,700;0,800;1,400&display=swap" rel="stylesheet">
<style>
  :root {
    --blue: #1a7bc2;
    --blue-deep: #1569a8;
    --panel-grey: #f2f2f5;
    --ink: #1b1b1f;
    --body: #3a3a40;
    --white: #ffffff;
    --backdrop: #e6e6e6;
    --icon: #55585e;
  }
  * { box-sizing: border-box; margin: 0; padding: 0; }
  html, body { width: 797px; height: 1200px; overflow: hidden; }
  body {
    background: var(--backdrop);
    font-family: "Poppins", sans-serif;
    color: var(--body);
    position: relative;
  }
  .spread { position: absolute; width: 577px; height: 446px; overflow: hidden; }
  .spread--outside { left: 106px; top: 92px; }
  .spread--inside { left: 117px; top: 611px; background: var(--panel-grey); }
  .abs { position: absolute; }

  /* Outside spread */
  .panel { position: absolute; top: 0; height: 446px; width: 193px; }
  .panel--about { left: 0; background: var(--panel-grey); }
  .panel--contact { left: 192px; background: var(--blue); }
  .panel--cover { left: 384px; background: var(--white); }

  .section-title { font-size: 11px; font-weight: 500; color: var(--ink); line-height: 1.2; }
  .section-title::after {
    content: ""; display: block; width: 30px; height: 1.5px;
    background: var(--blue); margin-top: 3px;
  }
  .section-title--light { color: var(--white); }
  .section-title--light::after { background: var(--white); }

  .body-copy { font-size: 7.3px; line-height: 10.2px; color: var(--body); }
  .body-copy--light { color: var(--white); }

  .about-title { left: 20px; top: 63px; }
  .about-p1 { left: 20px; top: 85px; width: 140px; }
  .about-p2 { left: 20px; top: 187px; width: 140px; }
  .quote-mark { left: 20px; top: 278px; width: 24px; height: 20px; }
  .quote-text {
    left: 39px; top: 307px; width: 120px;
    font-size: 9.6px; line-height: 10.9px; font-style: italic; color: var(--blue);
  }

  .contact-brand {
    left: 0; width: 193px; top: 108px; text-align: center; color: var(--white);
  }
  .contact-brand .brand-square {
    display: block; width: 10px; height: 10px; background: var(--white);
    margin: 0 auto 6px;
  }
  .contact-brand .brand-name { font-size: 12px; font-weight: 400; letter-spacing: 0.5px; }
  .contact-brand .brand-sub { font-size: 3.6px; letter-spacing: 0.4px; margin-top: 1px; }
  .contact-title {
    left: 0; width: 193px; top: 178px; text-align: center;
    font-size: 8.6px; font-weight: 500; color: var(--white);
  }
  .contact-title span { border-bottom: 1px solid var(--white); padding: 0 1px 1px; }
  .contact-intro {
    left: 46px; width: 101px; top: 195px; text-align: center;
    font-size: 6.6px; line-height: 8.8px; color: var(--white);
  }
  .contact-item { left: 0; width: 193px; text-align: center; font-size: 6.6px; line-height: 8.8px; color: var(--white); }
  .contact-icon { display: block; margin: 0 auto 5px; width: 11px; height: 11px; }
  .contact-item--phone { top: 236px; }
  .contact-item--fax { top: 267px; }
  .contact-item--address { top: 298px; }

  .cover-brand { left: 20px; top: 32px; display: flex; align-items: center; gap: 5px; }
  .cover-brand .brand-square { width: 24px; height: 21px; background: var(--blue); }
  .cover-brand .brand-name { font-size: 17.5px; font-weight: 800; color: var(--ink); letter-spacing: 0.2px; }
  .cover-photo {
    left: 0; top: 67px; width: 193px; height: 250px;
    background: linear-gradient(160deg, #5b8fc0 0%, #9bb8d6 45%, #d9dde6 75%, #4a6f98 100%);
  }
  .cover-band {
    left: 0; top: 316px; width: 193px; height: 14px; background: var(--blue);
    color: var(--white); font-size: 7.3px; line-height: 14px; padding-left: 20px;
  }
  .cover-title {
    left: 20px; top: 337px; font-size: 16.8px; line-height: 17.2px;
    font-weight: 700; color: var(--ink);
  }
  .cover-sub { left: 20px; top: 378px; font-size: 12px; color: var(--blue); }
  .cover-tag { left: 20px; top: 398px; width: 140px; font-size: 7.2px; line-height: 9.6px; font-style: italic; color: var(--ink); }

  /* Inside spread */
  .top-strip { left: 0; top: 0; width: 577px; height: 20px; background: var(--white); }
  .mission-block { left: 0; top: 20px; width: 192px; height: 209px; background: var(--blue); }
  .side-block { left: 535px; top: 20px; width: 42px; height: 209px; background: var(--blue); }
  .inside-photo {
    left: 192px; top: 0; width: 343px; height: 229px;
    background: linear-gradient(120deg, #2c3a3a 0%, #4f6a74 35%, #2f6fa8 60%, #8a939a 100%);
  }
  .mission-title { left: 20px; top: 64px; }
  .mission-copy { left: 20px; top: 84px; width: 140px; }
  .what-title { left: 20px; top: 238px; }
  .bottom-band { left: 0; top: 437px; width: 577px; height: 9px; background: var(--blue); }
  .fold { top: 229px; width: 6px; height: 208px; background: linear-gradient(90deg, rgba(0,0,0,0.03), rgba(0,0,0,0)); }

  .service { position: absolute; display: flex; }
  .service-icon { width: 20px; height: 20px; margin-top: 1px; }
  .service-body {
    border-left: 0.8px solid var(--blue); padding-left: 5px; margin-left: 9px;
    height: 46px; width: 110px;
  }
  .service-name { font-size: 7px; font-weight: 600; color: var(--ink); line-height: 9px; }
  .service-text { font-size: 6.7px; line-height: 8.7px; color: var(--body); margin-top: 1px; }
</style>
</head>
<body>

<section class="spread spread--outside">
  <div class="panel panel--about">
    <h2 class="abs section-title about-title">About Brindlecove</h2>
    <p class="abs body-copy about-p1">At Brindlecove, we do more than bridge the gap—we make the transition from hospital to home smooth and stress-free. From discharge to a patient’s appointment with their primary care physician, we coordinate every step, ensuring they receive the right care at the right time.</p>
    <p class="abs body-copy about-p2">For Medicare beneficiaries, this support is life-changing. Our personalized approach reduces readmissions, promotes faster recovery, and empowers patients with seamless, well-managed care from facility to home.</p>
    <svg class="abs quote-mark" viewBox="0 0 24 20" aria-hidden="true">
      <path d="M10 2 C4 3 1 7 1 12 a4 4 0 1 0 8 0 a4 4 0 0 0-4-4 C6 6 8 4 10 3Z M23 2 C17 3 14 7 14 12 a4 4 0 1 0 8 0 a4 4 0 0 0-4-4 C19 6 21 4 23 3Z" fill="var(--blue)"/>
    </svg>
    <p class="abs quote-text">Our process is simple, fast, and most importantly: effective. One call, and we take it from there. From your healthcare facility to their home, we’re there every step of the way.</p>
  </div>

  <div class="panel panel--contact">
    <div class="abs contact-brand">
      <span class="brand-square"></span>
      <div class="brand-name">BRINDLECOVE</div>
      <div class="brand-sub">POST ACUTE CARE</div>
    </div>
    <h3 class="abs contact-title"><span>Get In Touch</span></h3>
    <p class="abs contact-intro">Join us in transforming post-acute care. Let’s make every patient’s transition a story of success.</p>
    <div class="abs contact-item contact-item--phone">
      <svg class="contact-icon" viewBox="0 0 12 12" aria-hidden="true"><circle cx="6" cy="6" r="6" fill="var(--white)"/><path d="M4.2 3.3l.9-.2.6 1.4-.6.5a4 4 0 0 0 1.9 1.9l.5-.6 1.4.6-.2.9c-2.5.3-4.8-2-4.5-4.5z" fill="var(--blue)"/></svg>
      555-214-3870
    </div>
    <div class="abs contact-item contact-item--fax">
      <svg class="contact-icon" viewBox="0 0 12 12" aria-hidden="true"><circle cx="6" cy="6" r="6" fill="var(--white)"/><rect x="4" y="3" width="4" height="2" fill="var(--blue)"/><rect x="3" y="5.3" width="6" height="3.7" rx="0.6" fill="var(--blue)"/></svg>
      555-214-3871
    </div>
    <div class="abs contact-item contact-item--address">
      <svg class="contact-icon" viewBox="0 0 12 12" aria-hidden="true"><circle cx="6" cy="6" r="6" fill="var(--white)"/><path d="M6 2.8a2.2 2.2 0 0 0-2.2 2.2c0 1.6 2.2 4 2.2 4s2.2-2.4 2.2-4A2.2 2.2 0 0 0 6 2.8z" fill="var(--blue)"/><circle cx="6" cy="5" r="0.8" fill="var(--white)"/></svg>
      18 Harbor Ln, Ste 210,<br>Millbrook, MA, 01999
    </div>
  </div>

  <div class="panel panel--cover">
    <div class="abs cover-brand"><span class="brand-square"></span><span class="brand-name">BRINDLECOVE</span></div>
    <div class="abs cover-photo" role="img" aria-label="Nurse in blue scrubs pushing an elderly patient in a hospital gown in a wheelchair"></div>
    <div class="abs cover-band">Bridging Gaps &amp; Improving Lives</div>
    <h1 class="abs cover-title">Revolutionizing<br>Post-acute Care</h1>
    <p class="abs cover-sub">One patient at a time</p>
    <p class="abs cover-tag">Because every patient deserves a seamless recovery.</p>
  </div>
</section>

<section class="spread spread--inside">
  <div class="abs top-strip"></div>
  <div class="abs mission-block"></div>
  <div class="abs side-block"></div>
  <div class="abs inside-photo" role="img" aria-label="Nurse taking notes on a clipboard beside an older man using a walker in a clinic"></div>
  <h2 class="abs section-title section-title--light mission-title">Our Mission</h2>
  <p class="abs body-copy body-copy--light mission-copy">To make the healthcare experience for every patient as fluid, efficient, and compassionate as possible. Through cutting-edge care and seamless coordination, we ensure patients recover faster, stay healthier, and never lose sight of their well-being.</p>

  <h2 class="abs section-title what-title">What We Do</h2>
  <div class="abs fold" style="left:192px"></div>
  <div class="abs fold" style="left:384px"></div>

  <div class="service" style="left:20px;top:284px">
    <svg class="service-icon" viewBox="0 0 20 20" fill="none" stroke="var(--icon)" stroke-width="1"><rect x="1.5" y="6" width="12" height="9" rx="1"/><path d="M13.5 9h3l2 3v3h-5z"/><circle cx="5" cy="16" r="1.5"/><circle cx="15" cy="16" r="1.5"/><path d="M7.5 8v5M5 10.5h5"/></svg>
    <div class="service-body"><div class="service-name">Seamless Transition</div><div class="service-text">We ensure smooth facility-to-home transitions with no gaps in care, prioritizing patient outcomes.</div></div>
  </div>
  <div class="service" style="left:213px;top:284px">
    <svg class="service-icon" viewBox="0 0 20 20" fill="none" stroke="var(--icon)" stroke-width="1"><path d="M2 4v13M2 13h17v4M5 13v-3h13v3"/><circle cx="7" cy="8" r="1.5"/><path d="M4 2v6"/></svg>
    <div class="service-body"><div class="service-name">Reduced Readmission Risk</div><div class="service-text">We minimize readmission risk with proactive care, enhancing outcomes and supporting value-based care goals.</div></div>
  </div>
  <div class="service" style="left:405px;top:284px">
    <svg class="service-icon" viewBox="0 0 20 20" fill="none" stroke="var(--icon)" stroke-width="1"><circle cx="3.5" cy="3" r="1.5"/><circle cx="16.5" cy="3" r="1.5"/><circle cx="3.5" cy="15" r="1.5"/><circle cx="16.5" cy="15" r="1.5"/><rect x="7.5" y="7.5" width="5" height="5"/><path d="M5 5l2.5 2.5M15 5l-2.5 2.5M5 13l2.5-.5M15 13l-2.5-.5"/></svg>
    <div class="service-body"><div class="service-name">Streamlined Referral Process</div><div class="service-text">Easily refer patients with a fast, simple process that ensures seamless transitions in care.</div></div>
  </div>
  <div class="service" style="left:20px;top:357px">
    <svg class="service-icon" viewBox="0 0 20 20" fill="none" stroke="var(--icon)" stroke-width="1"><rect x="2" y="1.5" width="11" height="16" rx="1"/><path d="M4.5 5h6M4.5 8h6M4.5 11h4"/><rect x="12" y="11" width="5" height="7" rx="1"/></svg>
    <div class="service-body"><div class="service-name">Prescription Refills</div><div class="service-text">We handle refills for non-controlled prescriptions, ensuring your patients have what they need to recover.</div></div>
  </div>
  <div class="service" style="left:213px;top:357px">
    <svg class="service-icon" viewBox="0 0 20 20" fill="none" stroke="var(--icon)" stroke-width="1"><rect x="3" y="2.5" width="13" height="16" rx="1"/><rect x="7" y="1" width="5" height="3"/><path d="M6 8h7M6 11h7M6 14h5"/></svg>
    <div class="service-body"><div class="service-name">VNA Order Sign-Off</div><div class="service-text">We sign off on VNA orders, streamlining the process and ensuring seamless home care coordination.</div></div>
  </div>
  <div class="service" style="left:405px;top:357px">
    <svg class="service-icon" viewBox="0 0 20 20" fill="none" stroke="var(--icon)" stroke-width="1"><rect x="2" y="1.5" width="16" height="9" rx="1"/><path d="M5 6h3M6.5 4.5v3M11 5h5M11 7.5h4"/><circle cx="5" cy="13.5" r="1.5"/><circle cx="11" cy="13.5" r="1.5"/><path d="M2.5 18.5a2.5 2.5 0 0 1 5 0M8.5 18.5a2.5 2.5 0 0 1 5 0M15 14h3M15 17h3"/></svg>
    <div class="service-body"><div class="service-name">Patient Education</div><div class="service-text">Empowering patient’s with information to make informed decisions about their health.</div></div>
  </div>

  <div class="abs bottom-band"></div>
</section>

</body>
</html>
```